Varubo Highlands coffee needs bold, new coffee pack design

Having just developed a new logo (see attached file), we are now in the process of developing new coffee bag packaging designs. We are using a custom bag printer in the US, so the design will need will need to follow a specific art spec/template (which has also been uploaded). We will eventually need designs for two different coffee brands/types and two different size bags (essentially a 250g and 500g size). At this point, however, our goal is to develop a design for one size/coffee brand and from there work on variations for the others.
Updates

Project Deadline Extended
Reason: We are considering some small changes to the original design we outlined and want to allow extra time for current and new designers to make those tweaks. Thanks for your consideration of our coffee package project!

Hello, After reviewing some designs so far, and receiving additional feedback from test users in our market, we are making some changes to the template design. I have uploaded a new version of the template content, which has the following changes. 1. The two side panels are now without any text, but a visual design/pattern that you want to try there is still welcome. 2. The front and bag sections has been cleaned up a bit to have less text and more room for a visual design. 3. We would like to see stronger user of the following colors: red, yellow, black (which are Ugandan flag colors) and white. Some green as needed is allowed. 4. I have uploaded a map file showing Uganda including the Varubo region where the coffee comes from. Would like to incorporate this on the back side, ideally with a small Varubo Highlands logo pointing to the region in the bottom left in green or could even say something like "Home of Varubo Highlands Coffee.". Also the country should be titled "Uganda" to make that clear. With these changes, if you need more time on the design, let me know and we can look at extending the deadline. Thank you!

Hello, Although it is not showing just yet, we expect to have a one-week extension for this contest (so not ending on 29 September, but October 6). If you are working on a design, or re-design, please continue to do so as the contest will be extended. If you are interested in starting work, please do so. Thanks for your interest in our package design contest and I look forward to seeing your work soon. Doriel

Hello, Thank you to everyone who has submitted designs so far. We want to highlight two important items at this point: 1. Based on user feedback, we are changing the design considerations bit. The size and shape of the bags are not changing, but some of the creative content is. A new file has been uploaded entitled Coffee package content 250g size v3.pdf which details these changes. Please download and read that for updates. If you have any questions, please let me know. 2. Due to these changes, we are extending this contest for another week, so I'm hopeful you will have time to make changes and submit your new ideas! Thank you, Doriel

Target Market(s)

Varubo Highlands is a premium Ugandan coffee. We are targeting those drinkers who appreciate and seek out great coffee.

Industry/Entity Type

Printer

Font styles to use
Sans Serif

Colors
ec1f27
ffffff
9bcb3c
ffcf3e

Requirements
Must have
• The attached PDF file (coffee package content) design and content elements that need to be included. Designer has strong license to determine HOW they should be designed and shown. In terms of colors, would like to see strong use of red, black, yellow (Ugandan flag colors) and white. Green is also an option if needed.

The design file will need to follow specs that are detailed here:
http://www.pelmacrate.com/artwork_specs and be in the format shown in the uploaded file 5-8 oz Bag Template.pdf.
Nice to have
• Bag should be simple, but elegant. We did testing and found that too much information was distracting so we have pared down the design/content elements to the basics. Still, creative elements or patterns and overlays are very welcome.
Should not have
• The tone should be elegant and creative, but not hokey or too handmade looking. Watch the use of too many fonts and low-contrast colors with text on background.

```html
<!DOCTYPE html>
<html lang="en">
<head>
<meta charset="utf-8">
<title>Varubo Highlands – Dark Mountain Roast bag</title>
<link rel="stylesheet" href="https://fonts.googleapis.com/css2?family=Raleway:wght@400;600;700;800&family=Montserrat:wght@400;600;700;800&family=Open+Sans:wght@400;600&family=Playfair+Display:ital,wght@0,700;1,400&display=swap">
<style>
  :root{
    --red:#ec1f27;
    --red-dark:#b8141b;
    --yellow:#ffcf3e;
    --ink:#161616;
    --paper:#ffffff;
    --paper-grey:#efefef;
    --stage:#f4f4f4;
    --green:#2e9a2a;
    --muted:#444;
  }
  *{box-sizing:border-box;margin:0;padding:0}
  html,body{width:1200px;height:1000px;overflow:hidden;background:var(--stage)}
  body{position:relative;font-family:"Montserrat",sans-serif;color:var(--ink)}

  .panel{position:absolute;top:70px;height:860px;overflow:hidden;box-shadow:0 10px 30px rgba(0,0,0,.12)}

  /* FRONT */
  .front{left:50px;width:470px;background:linear-gradient(#ffffff 0%,#f3f3f3 38%)}
  .brand{position:absolute;top:62px;left:0;right:0;text-align:center}
  .brand-mark{width:70px;height:70px;border-radius:50%;background:var(--ink);margin:0 auto 22px}
  .brand-name{font-family:"Raleway",sans-serif;font-weight:700;font-size:44px;color:var(--red);letter-spacing:.5px;line-height:1}
  .brand-tag{font-family:"Raleway",sans-serif;font-weight:700;font-size:12px;letter-spacing:3.5px;color:var(--ink);margin-top:8px}

  .front-photo{position:absolute;top:290px;left:0;right:0;bottom:0;
    background:linear-gradient(180deg,#c9d3b4 0%,#8aa262 22%,#9cb56a 45%,#6f8a4a 62%,#9b7a4a 82%,#6e5032 100%)}
  .roast-title{position:absolute;top:400px;left:32px;font-family:"Raleway",sans-serif;line-height:.95;color:var(--ink)}
  .roast-title .bold{display:block;font-weight:800;font-size:46px}
  .roast-title .light{display:block;font-weight:400;font-size:46px}
  .roast-scale{position:absolute;top:560px;left:32px;display:flex;border:2px solid var(--ink);border-radius:3px;height:30px;align-items:center;background:rgba(255,255,255,.55)}
  .roast-scale span{font-family:"Raleway",sans-serif;font-weight:700;font-size:13px;padding:0 10px;color:var(--ink);height:100%;display:flex;align-items:center}
  .roast-scale .is-active{background:var(--red);color:var(--paper)}
  .roast-note{position:absolute;top:602px;left:32px;font-family:"Raleway",sans-serif;font-weight:800;font-size:15px;color:var(--ink);line-height:1.15;background:var(--yellow);padding:4px 8px}
  .front-band{position:absolute;left:0;right:0;bottom:0;height:46px;background:var(--ink);display:flex;align-items:center;padding:0 16px;gap:16px;color:var(--paper);font-family:"Raleway",sans-serif;font-size:15px;border-top:4px solid var(--red)}
  .check{display:flex;align-items:center;gap:7px}
  .check svg{width:16px;height:16px}
  .net-wt{margin-left:auto;font-weight:800;font-size:14px;line-height:1.05;text-align:right;color:var(--yellow)}

  /* BACK */
  .back{left:560px;width:500px;background:linear-gradient(160deg,var(--paper) 0%,var(--paper-grey) 100%)}
  .name-head{position:absolute;top:52px;left:0;right:0;text-align:center;font-family:"Montserrat",sans-serif;font-weight:700;color:var(--ink);letter-spacing:2px;font-size:15px;line-height:1.6}
  .name-head .dot{color:var(--red)}
  .ribbon{position:absolute;top:118px;left:95px;width:310px;height:30px;background:var(--red);color:var(--paper);font-weight:700;font-size:16px;letter-spacing:2px;display:flex;align-items:center;justify-content:center;outline:2px solid var(--red);outline-offset:3px}
  .story{position:absolute;top:180px;left:40px;right:40px;font-family:"Open Sans",sans-serif;font-size:13px;line-height:1.5;color:var(--ink);text-align:justify}
  .story p+p{margin-top:14px}
  .brew{position:absolute;top:400px;left:40px;display:flex;align-items:center;gap:10px;font-family:"Playfair Display",serif;font-style:italic;font-size:20px;color:var(--ink)}
  .brew-tag{background:var(--ink);color:var(--yellow);font-family:"Raleway",sans-serif;font-style:normal;font-weight:700;font-size:15px;padding:5px 14px}
  .map{position:absolute;top:455px;left:110px;width:350px;height:310px;border-radius:46% 40% 44% 38%;background:radial-gradient(ellipse at 55% 55%,#f6f6f6 0%,#dfe7ea 55%,#c6d6dc 100%);box-shadow:inset 0 0 0 2px rgba(22,22,22,.35)}
  .map-label{position:absolute;top:615px;left:300px;font-family:"Montserrat",sans-serif;font-weight:800;font-size:17px;color:var(--ink);letter-spacing:1px}
  .home-badge{position:absolute;top:590px;left:35px;width:175px;padding:10px 8px;background:var(--green);color:var(--paper);text-align:center;font-family:"Raleway",sans-serif;border:2px solid var(--paper);outline:2px solid var(--green)}
  .home-badge .small{font-size:12px;font-style:italic}
  .home-badge .big{font-weight:700;font-size:16px;line-height:1.15}
  .pointer{position:absolute;top:668px;left:116px;width:12px;height:92px;background:var(--green)}
  .enjoy{position:absolute;bottom:30px;left:40px;text-align:center;font-family:"Raleway",sans-serif}
  .enjoy .rule{border-top:1px solid var(--ink);border-bottom:1px solid var(--ink);font-family:"Playfair Display",serif;font-style:italic;font-size:17px;padding:2px 18px;color:var(--red)}
  .enjoy .best{font-weight:800;font-size:20px;margin-top:4px}
  .ugandan{position:absolute;bottom:36px;left:235px;width:150px;height:56px;background:var(--ink);color:var(--yellow);font-family:"Playfair Display",serif;font-weight:700;font-size:17px;line-height:1.05;display:flex;flex-direction:column;align-items:center;justify-content:center;letter-spacing:1px;border-bottom:4px solid var(--red)}

  /* SIDE GUSSET */
  .side{left:1060px;width:100px;background:linear-gradient(90deg,var(--red-dark),var(--red));color:var(--paper);font-family:"Raleway",sans-serif;padding:220px 9px 0}
  .side .thanks{font-size:11px;font-weight:700;line-height:1.25}
  .side .ask{font-size:12px;font-weight:800;margin-top:24px;line-height:1.2;color:var(--yellow)}
  .side .love{font-size:10px;margin-top:8px;line-height:1.25}
  .side dt{font-size:10px;font-weight:800;margin-top:18px;letter-spacing:1px;color:var(--yellow)}
  .side dd{font-size:9.5px;line-height:1.3;margin-top:3px}
</style>
</head>
<body>

<section class="panel front">
  <header class="brand">
    <div class="brand-mark"></div>
    <div class="brand-name">Varubo Highlands</div>
    <div class="brand-tag">PREMIUM UGANDAN COFFEE</div>
  </header>

  <div class="front-photo" role="img" aria-label="Photograph of terraced highland hills with a coffee farmer holding freshly picked red coffee cherries"></div>

  <h1 class="roast-title"><span class="bold">DARK</span><span class="bold">MOUNTAIN</span><span class="light">ROAST</span></h1>

  <div class="roast-scale">
    <span>LIGHT</span><span class="is-active">•MEDIUM•</span><span>DARK</span><span>VERY DARK</span>
  </div>
  <p class="roast-note">OUR BOLD, RICH 100%<br>ARABICA ROAST</p>

  <footer class="front-band">
    <span class="check">
      <svg viewBox="0 0 16 16"><rect x="1" y="1" width="14" height="14" fill="none" stroke="#fff" stroke-width="1.5"/><path d="M4 8l3 3 5-6" fill="none" stroke="#ffcf3e" stroke-width="2"/></svg>
      WHOLE BEAN
    </span>
    <span class="check">
      <svg viewBox="0 0 16 16"><rect x="1" y="1" width="14" height="14" fill="none" stroke="#fff" stroke-width="1.5"/></svg>
      GROUND
    </span>
    <span class="net-wt">NET WT:<br>250G / 9OZ.</span>
  </footer>
</section>

<section class="panel back">
  <h2 class="name-head">
    <div>WHAT DOES OUR NAME</div>
    <div><span class="dot">•</span> SAY ABOUT COFFEE? <span class="dot">•</span></div>
  </h2>
  <div class="ribbon">...EVERYTHING.</div>

  <div class="story">
    <p>The Varubo Highlands of Southwest Uganda produces exceptional coffee. Pure highland air blends with abundant sun, rain and fertile volcanic soils to produce remarkable beans with rich, bold complex flavors.</p>
    <p>More than 3,000 area farmers carefully select only the best beans, which are then dried and hand-roasted to become Varubo Highlands, a premium 100% Ugandan coffee.</p>
  </div>

  <div class="brew">Brew the Perfect cup of <span class="brew-tag">Varubo Highlands</span></div>

  <div class="map" role="img" aria-label="Map of Uganda with lakes, rivers, towns and the Varubo region marked in the southwest"></div>
  <div class="map-label">UGANDA</div>
  <div class="pointer"></div>
  <div class="home-badge">
    <div class="small">Home of</div>
    <div class="big">Varubo Highlands</div>
    <div class="big">COFFEE</div>
  </div>

  <div class="enjoy">
    <div class="rule">Enjoy</div>
    <div class="best">THE BEST OF</div>
  </div>
  <div class="ugandan"><span>UGANDAN</span><span>COFFEE</span></div>
</section>

<aside class="panel side">
  <p class="thanks">Thank you for buying Varubo Highlands Coffee</p>
  <p class="ask">Questions or Comments?</p>
  <p class="love">We'd love to hear from you!</p>
  <dl>
    <dt>ADDRESS</dt>
    <dd>Pelmara Ltd, 14 Nsambo Crescent, Kampala, Uganda</dd>
    <dt>PHONE</dt>
    <dd>+256 700 418 220</dd>
    <dt>ONLINE</dt>
    <dd>varubo.coffee</dd>
    <dt>EMAIL</dt>
    <dd>hi@varubo.coffee</dd>
  </dl>
</aside>

</body>
</html>
```